Brambury Logistics

Create a modern, simple, Elegant business card design for my business.

Services: Tamo Trucks, Transport, Contract Logistics,

Industry/Entity Type

Business

Contact Information for Business Card

Include all details same as old card plus new website address: www.bramburylogistics.com.au

Requirements
Must have
• Similar colors to Logo.

```html
<!DOCTYPE html>
<html lang="en">
<head>
<meta charset="utf-8">
<title>Brambury Logistics — Business Card</title>
<link rel="stylesheet" href="https://fonts.googleapis.com/css2?family=Open+Sans:wght@400;600;700&display=swap">
<style>
  :root {
    --bg: #e9eaec;
    --card-white: #ffffff;
    --brand-blue: #1a6fae;
    --brand-blue-dark: #0e4f86;
    --brand-blue-light: #1fa3dc;
    --text-grey: #5e6266;
    --band-grey: #55595d;
    --white: #ffffff;
  }
  * { box-sizing: border-box; margin: 0; padding: 0; }
  html, body { width: 1200px; height: 1000px; overflow: hidden; }
  body {
    background: var(--bg);
    font-family: "Open Sans", Arial, sans-serif;
    position: relative;
  }
  .card {
    position: absolute;
    left: 265px;
    width: 667px;
    height: 396px;
    box-shadow: 0 4px 14px rgba(0,0,0,0.25);
    overflow: hidden;
  }
  .card--front { top: 75px; background: var(--card-white); }
  .card--back {
    top: 533px;
    background: linear-gradient(30deg, var(--brand-blue-light) 0%, #1581bd 50%, #0a5a8e 100%);
  }
  .wordmark {
    position: absolute;
    font-weight: 700;
    white-space: nowrap;
    letter-spacing: -0.5px;
  }
  .card--front .wordmark {
    left: 33px; top: 38px;
    font-size: 40px;
    color: var(--brand-blue);
  }
  .card--back .wordmark {
    left: 0; right: 0; top: 150px;
    text-align: center;
    font-size: 54px;
    color: var(--white);
  }
  .contact { position: absolute; left: 33px; top: 170px; }
  .contact__name {
    font-size: 23px; font-weight: 700; color: var(--brand-blue);
    letter-spacing: 0.3px;
  }
  .contact__title { font-size: 16px; color: var(--text-grey); margin-top: 2px; }
  .contact__list { list-style: none; margin-top: 17px; }
  .contact__list li {
    display: flex; align-items: center; gap: 8px;
    font-size: 16px; color: var(--text-grey); line-height: 22.5px;
  }
  .contact__list svg { width: 14px; height: 14px; fill: var(--brand-blue); flex: none; }
  .contact__address { margin-top: 3px; font-size: 16px; color: var(--text-grey); padding-left: 2px; }
  .services { position: absolute; left: 410px; top: 163px; }
  .services__heading { font-size: 21px; font-weight: 700; color: var(--brand-blue); }
  .services__list { list-style: none; margin-top: 4px; }
  .services__list li {
    position: relative; padding-left: 22px;
    font-size: 15.5px; color: var(--text-grey); line-height: 22.3px;
  }
  .services__list svg {
    position: absolute; left: 0; top: 5px; width: 14px; height: 12px;
    fill: none; stroke: var(--brand-blue); stroke-width: 2.2;
  }
  .front-band {
    position: absolute; left: 0; bottom: 0; width: 667px; height: 36px;
    background: linear-gradient(90deg, var(--card-white) 20%, #a9acaf 60%, var(--band-grey) 100%);
  }
  .front-band__url {
    position: absolute; right: 32px; top: 7px;
    font-size: 15.5px; color: var(--white);
  }
  .back-url {
    position: absolute; left: 0; right: 0; top: 348px;
    text-align: center; font-size: 15.5px; color: var(--white);
  }
</style>
</head>
<body>

<section class="card card--front">
  <div class="wordmark">Brambury Logistics</div>

  <div class="contact">
    <div class="contact__name">DANA WHITCOMBE</div>
    <div class="contact__title">Chief Executive Officer</div>
    <ul class="contact__list">
      <li><svg viewBox="0 0 14 14"><rect x="4" y="0" width="6" height="14" rx="1"/><rect x="5.3" y="2" width="3.4" height="4" fill="#fff"/></svg>+ 000 000 0000</li>
      <li><svg viewBox="0 0 14 14"><rect x="3" y="0" width="8" height="4"/><rect x="0" y="5" width="14" height="6" rx="1"/><rect x="3" y="9" width="8" height="5"/></svg>+ 000 000 0000</li>
      <li><svg viewBox="0 0 14 14"><rect x="0" y="3" width="14" height="9"/><path d="M0 3 L7 8.5 L14 3" stroke="#fff" stroke-width="1.3" fill="none"/></svg>www.bramburylogistics.com.au</li>
    </ul>
    <div class="contact__address">4180 W. Harlow Ave. Denton, TX 76201</div>
  </div>

  <div class="services">
    <div class="services__heading">SERVICES</div>
    <ul class="services__list">
      <li><svg viewBox="0 0 14 12"><path d="M1 6 L5 10 L13 1"/></svg>Tamo Trucks</li>
      <li><svg viewBox="0 0 14 12"><path d="M1 6 L5 10 L13 1"/></svg>Specialized Transport</li>
      <li><svg viewBox="0 0 14 12"><path d="M1 6 L5 10 L13 1"/></svg>Contract Logistics</li>
      <li><svg viewBox="0 0 14 12"><path d="M1 6 L5 10 L13 1"/></svg>Express // Hotshot Services</li>
      <li><svg viewBox="0 0 14 12"><path d="M1 6 L5 10 L13 1"/></svg>All Gerneral and Oversize<br>Transport</li>
    </ul>
  </div>

  <div class="front-band">
    <div class="front-band__url">www.bramburylogistics.com.au</div>
  </div>
</section>

<section class="card card--back">
  <div class="wordmark">Brambury Logistics</div>
  <div class="back-url">www.bramburylogistics.com.au</div>
</section>

</body>
</html>
```